Corporate Design für Hausverwalterin und Immobilienvermarktung
Zielgruppe
Hausverwalterin und Immobilienvermarktung
Aufgabenstellung
wir sind im Immobiliensektor unterwegs und das Design soll edel und hochwertig sein

```html
<!DOCTYPE html>
<html lang="de">
<head>
<meta charset="utf-8">
<title>Halden Immobilien – Visitenkarte</title>
<link rel="stylesheet" href="https://fonts.googleapis.com/css2?family=Montserrat:wght@600;700&display=swap">
<style>
  :root {
    --navy: #15293c;
    --gold: #d5b36a;
    --white: #ffffff;
    --page: #ffffff;
  }
  * { margin: 0; padding: 0; box-sizing: border-box; }
  html, body {
    width: 1200px; height: 1200px; overflow: hidden;
    background: var(--page);
    font-family: "Montserrat", Arial, sans-serif;
  }
  .card {
    position: absolute; left: 219px; width: 770px; height: 440px;
    background: var(--navy);
    box-shadow: 0 8px 28px rgba(0,0,0,0.22);
  }
  .card--front { top: 128px; }
  .card--back { top: 639px; }

  /* Front */
  .brand {
    position: absolute; left: 0; width: 424px; top: 246px;
    text-align: center; color: var(--gold);
  }
  .brand__row {
    display: flex; align-items: center; justify-content: center; gap: 10px;
  }
  .brand__square { width: 18px; height: 18px; background: var(--gold); }
  .brand__name {
    font-weight: 700; font-size: 27px; letter-spacing: 1px;
    text-transform: uppercase; line-height: 1;
  }
  .brand__tagline {
    margin-top: 8px; font-weight: 600; font-size: 9.5px;
    letter-spacing: 1.2px; text-transform: uppercase;
  }
  .divider {
    position: absolute; left: 423px; top: 73px; width: 2px; height: 295px;
    background: var(--gold);
  }
  .contact { position: absolute; left: 473px; top: 164px; list-style: none; }
  .contact__item {
    display: flex; align-items: center; height: 24px; margin-bottom: 20px;
    color: var(--gold); font-weight: 600; font-size: 16.5px;
  }
  .contact__icon { width: 18px; height: 18px; margin-right: 10px; fill: var(--gold); }

  /* Back */
  .pitch {
    position: absolute; left: 0; right: 0; top: 76px;
    text-align: center; text-transform: uppercase;
    font-weight: 700; font-size: 17.5px; line-height: 20.8px; letter-spacing: 0.4px;
  }
  .pitch p + p { margin-top: 20.8px; }
  .gold { color: var(--gold); }
  .white { color: var(--white); }
</style>
</head>
<body>
  <section class="card card--front">
    <div class="brand">
      <div class="brand__row">
        <span class="brand__square"></span>
        <span class="brand__name">Halden Immobilien</span>
      </div>
      <div class="brand__tagline">Verwaltung und Vermarktung</div>
    </div>
    <div class="divider"></div>
    <ul class="contact">
      <li class="contact__item">
        <svg class="contact__icon" viewBox="0 0 24 24"><path d="M6.6 10.8a15.1 15.1 0 0 0 6.6 6.6l2.2-2.2a1 1 0 0 1 1-.25 11.4 11.4 0 0 0 3.6.57 1 1 0 0 1 1 1V20a1 1 0 0 1-1 1A17 17 0 0 1 3 4a1 1 0 0 1 1-1h3.5a1 1 0 0 1 1 1c0 1.25.2 2.45.57 3.57a1 1 0 0 1-.25 1z"/></svg>
        0151 482 19 07
      </li>
      <li class="contact__item">
        <svg class="contact__icon" viewBox="0 0 24 24"><path d="M2 5h20v14H2z M3.5 6.5 12 13l8.5-6.5" fill="none" stroke="#d5b36a" stroke-width="2"/></svg>
        info@halden-immobilien.de
      </li>
      <li class="contact__item">
        <svg class="contact__icon" viewBox="0 0 24 24"><g fill="none" stroke="#d5b36a" stroke-width="1.8"><circle cx="12" cy="12" r="9"/><ellipse cx="12" cy="12" rx="4" ry="9"/><path d="M3 12h18M5 7h14M5 17h14"/></g></svg>
        www.halden-immobilien.de
      </li>
    </ul>
  </section>

  <section class="card card--back">
    <div class="pitch">
      <p class="gold">Ganzheitliche Immobilienbetreuung mit Strategie.</p>
      <p class="white">Als zertifizierte Hausverwalterin &amp; Immobilienmaklerin<br>gemäß § 34c GewO verbinde ich klassische<br>Verwaltung mit wertoptimierter Vermarktung:</p>
      <p class="gold">- Hausverwaltung: rechtssicher &amp; entlastend.<br>- Asset Management: strategische Ertragssteigerung.<br>- Verkauf: marktgerecht &amp; professionell.</p>
      <p><span class="white">Telefon: 0151 482 19 07</span><br><span class="gold">Halden Immobilien - Ihr Eigentum in zuverlässigen Händen.</span><br><span class="white">E-Mail: info@halden-immobilien.de</span><br><span class="white">Webseite: www.halden-immobilien.de</span></p>
    </div>
  </section>
</body>
</html>
```